High End Notary Service Business Card Design

Want a professional and elegant/luxurious business card that is clean and simple in the design. A notary is a trusted professional that helps people sign very important documents. The card should be in alignment with this service provided.

Most of the time, service will be for the purchase of a home or refinance of a mortgage

There is NO LOGO. This is aesthetic. A look and feel. Conveying professionalism and concierge level of service.

Target Market(s)

Other business professionals, Lawyers, Escrow Officers, Loan Officers

Industry/Entity Type

Legal

Contact Information for Business Card

This will be a one-sided business card

Colors
35a7d7
3176b5
85cae6
d3a5cc
b868aa
ffffff
0356a4

Requirements
Must have
• Lorena T. Mirabel-Hodgkins
Notary Public

642-871-3094
MirabelSigningDesk@Wexmail.com
Nice to have
• Headshot photo below. Convey the aspect of signing documents. No black cards. Preference is shades of blue: light blue, navy, aqua, gold, white, or lavendar, etc.
Should not have
• No scales or legal scales.

```html
<!DOCTYPE html>
<html lang="en">
<head>
<meta charset="UTF-8">
<title>Lorena T. Mirabel-Hodgkins — Notary Public</title>
<link rel="stylesheet" href="https://fonts.googleapis.com/css2?family=Bodoni+Moda:wght@400;500&family=Mrs+Saint+Delafield&display=swap">
<style>
  :root {
    --page-bg: #f2f1f3;
    --card-light: #efd9ec;
    --card-mid: #e3bfde;
    --card-deep: #c993c2;
    --ink: #c66dba;
    --ring: rgba(255, 255, 255, 0.22);
  }
  * { margin: 0; padding: 0; box-sizing: border-box; }
  html, body {
    width: 1200px;
    height: 900px;
    overflow: hidden;
    background: var(--page-bg);
  }
  .canvas {
    position: relative;
    width: 1200px;
    height: 900px;
    display: flex;
    align-items: center;
    justify-content: center;
  }
  .business-card {
    position: relative;
    width: 1050px;
    height: 600px;
    overflow: hidden;
    background: radial-gradient(ellipse 70% 80% at 48% 28%, var(--card-light) 0%, var(--card-mid) 55%, var(--card-deep) 100%);
    box-shadow: 0 10px 30px rgba(80, 40, 80, 0.18);
  }
  .decor-rings {
    position: absolute;
    inset: 0;
    width: 100%;
    height: 100%;
  }
  .contact {
    position: absolute;
    left: 540px;
    top: 190px;
    font-family: "Bodoni Moda", serif;
    font-size: 23px;
    line-height: 1.5;
    color: var(--ink);
    white-space: nowrap;
  }
  .identity {
    position: absolute;
    left: 70px;
    top: 320px;
    color: var(--ink);
  }
  .identity-name {
    font-family: "Bodoni Moda", serif;
    font-weight: 500;
    font-size: 52px;
    line-height: 1.1;
    white-space: nowrap;
  }
  .identity-title {
    font-family: "Mrs Saint Delafield", cursive;
    font-weight: 400;
    font-size: 64px;
    line-height: 1;
    margin-top: 22px;
    margin-left: -6px;
    white-space: nowrap;
  }
</style>
</head>
<body>
  <main class="canvas">
    <section class="business-card">
      <svg class="decor-rings" viewBox="0 0 1050 600" aria-hidden="true">
        <circle cx="200" cy="480" r="210" fill="none" stroke="var(--ring)" stroke-width="34"/>
        <circle cx="960" cy="250" r="185" fill="none" stroke="var(--ring)" stroke-width="34"/>
      </svg>
      <div class="contact">
        <p class="contact-phone">Tel. 642-871-3094</p>
        <p class="contact-email">E-mail. MirabelSigningDesk@Wexmail.com</p>
      </div>
      <div class="identity">
        <h1 class="identity-name">Lorena T. Mirabel-Hodgkins</h1>
        <p class="identity-title">Notary Public</p>
      </div>
    </section>
  </main>
</body>
</html>
```